Knee Wraps

brand name is velmo
300g package
collagen product containing bovine collagen peptides
orange packaging color
with turmeric added
ultimate complex for joints flexibility & mobility
ingredients
collagen, turmeric curcumin, vitamin c
a product that takes care of the joints mobility and provides resilience against injuries

similar design to the packaging in the files

Target Market(s)

fitness, health products

Industry/Entity Type

health and fitness

Colors
F0912C
F2A743
F7CA91
FBE8D2
FDF5EE

Requirements
Must have
• very clear message of the advantage of the product which is providing flexible joints, increased mobility, great inflammation response, amazing skin hair bones and nails care
Nice to have
• turmeric design or something that indicates the product containing organic turmeric, orange fresh design, something to makes me feel happy with movement of my body/joints

```html
<!DOCTYPE html>
<html lang="en">
<head>
<meta charset="utf-8">
<title>velmo Collagen Peptides – Pouch Label</title>
<link rel="stylesheet" href="https://fonts.googleapis.com/css2?family=Big+Shoulders+Display:wght@600;700&family=Source+Serif+4:wght@400;600;700&display=swap">
<style>
  :root {
    --sun: #FDD06A;
    --amber: #F7A935;
    --orange: #F5921F;
    --deep-orange: #E8821E;
    --logo-yellow: #FCD266;
    --badge-text: #F0A43C;
    --icon-fill: #FBC862;
    --white: #FFFFFF;
    --canvas: #FFFFFF;
  }
  * { box-sizing: border-box; margin: 0; padding: 0; }
  html, body { width: 1200px; height: 965px; overflow: hidden; background: var(--canvas); }
  .canvas { position: relative; width: 1200px; height: 965px; overflow: hidden; background: var(--canvas); }

  .label {
    position: absolute; left: 0; top: 0; width: 860px; height: 965px;
    background: linear-gradient(180deg, var(--sun) 0%, var(--amber) 30%, var(--orange) 55%, var(--orange) 100%);
  }
  .label__band {
    position: absolute; left: 238px; top: 0; width: 200px; height: 450px; background: var(--white);
  }
  .title-line {
    position: absolute; left: 238px; width: 200px; text-align: center; white-space: nowrap;
    font-family: "Big Shoulders Display", "Arial Narrow", sans-serif; font-weight: 700; line-height: 1;
  }
  .title-line span { display: inline-block; transform-origin: center center; }
  .brand-name { top: 150px; font-size: 132px; color: var(--logo-yellow); }
  .brand-name span { transform: scaleX(0.62); }
  .product-title { margin: 0; }
  .product-title__line { font-size: 80px; color: var(--deep-orange); line-height: 0.82; }
  .product-title__line--one { top: 280px; }
  .product-title__line--one span { transform: scaleX(0.7); }
  .product-title__line--two { top: 345px; }
  .product-title__line--two span { transform: scaleX(0.78); }

  .turmeric-art { position: absolute; left: 216px; top: 400px; width: 250px; height: 214px; }
  .badge {
    position: absolute; left: 190px; top: 452px; width: 88px; height: 88px; border-radius: 50%;
    background: var(--white); display: flex; align-items: center; justify-content: center; text-align: center;
    font-family: "Source Serif 4", Georgia, serif; font-weight: 600; font-size: 17px; line-height: 0.98;
    color: var(--badge-text);
  }
  .benefits { position: absolute; top: 630px; left: 0; width: 860px; height: 90px; }
  .benefit {
    position: absolute; top: 0; width: 160px; margin-left: -80px; text-align: center;
    font-family: "Source Serif 4", Georgia, serif; font-weight: 600; font-size: 13px; line-height: 1.12; color: var(--white);
  }
  .benefit svg { display: block; margin: 0 auto 6px; }
  .benefit--skin { left: 192px; }
  .benefit--joints { left: 337px; }
  .benefit--inflammation { left: 490px; }
  .divider { position: absolute; top: 24px; width: 2px; height: 48px; background: var(--white); }
  .divider--one { left: 260px; }
  .divider--two { left: 413px; }
  .ingredients {
    position: absolute; left: 177px; top: 738px; width: 324px; height: 64px; border: 3px solid var(--white);
    text-align: center; color: var(--white); font-family: "Source Serif 4", Georgia, serif; font-size: 15.5px; line-height: 1.08;
    padding-top: 5px;
  }
  .ingredients__title { font-weight: 700; }
  .net-weight {
    position: absolute; left: 177px; top: 818px; width: 324px; text-align: center;
    font-family: "Source Serif 4", Georgia, serif; font-weight: 700; font-size: 15.5px; color: var(--white);
  }
</style>
</head>
<body>
<main class="canvas">
  <section class="label">
    <div class="label__band"></div>
    <div class="title-line brand-name"><span>velmo</span></div>
    <h1 class="product-title">
      <span class="title-line product-title__line product-title__line--one"><span>COLLAGEN</span></span>
      <span class="title-line product-title__line product-title__line--two"><span>PEPTIDES</span></span>
    </h1>
    <svg class="turmeric-art" role="img" aria-label="Engraved illustration of turmeric roots and leaves" viewBox="0 0 250 214">
      <defs>
        <radialGradient id="turmericTone" cx="50%" cy="55%" r="55%">
          <stop offset="0%" stop-color="#FBCB6A"/>
          <stop offset="70%" stop-color="#F8BA50" stop-opacity="0.75"/>
          <stop offset="100%" stop-color="#F5A33A" stop-opacity="0"/>
        </radialGradient>
      </defs>
      <ellipse cx="125" cy="112" rx="125" ry="100" fill="url(#turmericTone)"/>
    </svg>
    <div class="badge">with<br>turmeric<br>added</div>

    <div class="benefits">
      <div class="benefit benefit--skin">
        <svg width="100" height="42" viewBox="0 0 100 42" aria-hidden="true">
          <circle cx="26" cy="24" r="17" fill="var(--icon-fill)"/>
          <rect x="9" y="22" width="34" height="4" fill="#fff"/>
          <circle cx="48" cy="24" r="17" fill="var(--icon-fill)"/>
          <path d="M38 36 L52 10 M44 38 L58 12" stroke="#fff" stroke-width="3"/>
          <circle cx="72" cy="24" r="17" fill="var(--icon-fill)"/>
          <rect x="67" y="14" width="10" height="16" rx="5" fill="#fff"/>
          <path d="M14 6h6M17 3v6M82 4h6M85 1v6M92 32h6M95 29v6" stroke="#fff" stroke-width="2"/>
        </svg>
        Skin, hair, &amp; nails<br>care
      </div>
      <div class="divider divider--one"></div>
      <div class="benefit benefit--joints">
        <svg width="60" height="42" viewBox="0 0 60 42" aria-hidden="true">
          <circle cx="30" cy="22" r="19" fill="var(--icon-fill)"/>
          <path d="M22 36 L30 24 M32 20 L42 6" stroke="#fff" stroke-width="4" stroke-linecap="round"/>
          <circle cx="31" cy="22" r="4" fill="#fff"/>
        </svg>
        ultimate complex<br>for joints flexibility<br>&amp; mobility
      </div>
      <div class="divider divider--two"></div>
      <div class="benefit benefit--inflammation">
        <svg width="60" height="42" viewBox="0 0 60 42" aria-hidden="true">
          <circle cx="30" cy="22" r="19" fill="var(--icon-fill)"/>
          <path d="M17 24 L25 16 L31 21 L41 11 M35 11 h6 v6" stroke="#fff" stroke-width="2.5" fill="none"/>
          <path d="M12 28 h36" stroke="#fff" stroke-width="2"/>
        </svg>
        Super inflammatory<br>response
      </div>
    </div>

    <div class="ingredients">
      <div class="ingredients__title">ingredients:</div>
      <div>collagen, turmeric curcumin,<br>vitamin c, glucoasmine, hyaluronic acid</div>
    </div>
    <div class="net-weight">NET WT 11 oz / 300 gr</div>
  </section>
</main>
</body>
</html>
```